BRIM Outreach Partners Business Card Rebrand

Hello Designers! We are looking for help designing our new business card to go in conjunction with our company rebrand. Unfortunately, we have an event mid June that requires we get these printed ASAP (before our new website is launched.) We have a mostly complete Brand Book which I have uploaded to this request for your reference to company information, style, fonts. I've also enclosed our logo file in .eps & .jpg. Attached is a sample business card my boss liked but said was "too simple." I made it in Canva and do not profess to be a designer. NOT FOR DESIGN REFERENCE, ONLY FOR CONTEXT Here is what our old website looks like: https://brimoutreachpartners.com/.

```html
<!DOCTYPE html>
<html lang="en">
<head>
<meta charset="utf-8">
<title>BRIM Outreach Partners — Business Card</title>
<link rel="stylesheet" href="https://fonts.googleapis.com/css2?family=Montserrat:wght@700&family=Quicksand:wght@500;700&display=swap">
<style>
  :root {
    --sky: #4ab3e6;
    --sky-deep: #3ea6da;
    --ink: #111111;
    --paper: #ffffff;
    --backdrop: #e9ebee;
    --muted: #2a2a2a;
  }
  * { box-sizing: border-box; margin: 0; padding: 0; }
  html, body { width: 1200px; height: 900px; overflow: hidden; }
  body {
    background: var(--backdrop);
    font-family: "Quicksand", sans-serif;
    position: relative;
  }
  .card {
    position: absolute;
    left: 230px;
    width: 740px;
    height: 423px;
    border-radius: 26px;
    overflow: hidden;
    box-shadow: 0 6px 20px rgba(0,0,0,0.12);
  }
  /* Front */
  .card-front { top: 24px; background: var(--sky); }
  .front-pattern {
    position: absolute; inset: 0;
    background: linear-gradient(135deg, #5cbdea 0%, var(--sky) 45%, var(--sky-deep) 100%);
  }
  .front-lockup {
    position: absolute;
    left: 380px; top: 170px;
    display: flex; align-items: center; gap: 18px;
  }
  .lockup-dot {
    width: 76px; height: 76px; border-radius: 50%;
    background: var(--paper);
  }
  .wordmark {
    font-family: "Montserrat", sans-serif;
    font-weight: 700;
    color: var(--ink);
    line-height: 1.02;
    letter-spacing: -0.5px;
  }
  .front-lockup .wordmark { font-size: 30px; }

  /* Back */
  .card-back { top: 466px; background: var(--paper); }
  .back-tab {
    position: absolute; right: 120px; top: 0;
    width: 26px; height: 18px; background: var(--sky);
  }
  .back-wordmark {
    position: absolute; left: 48px; top: 70px;
    font-size: 40px;
  }
  .person {
    position: absolute; right: 250px; top: 46px; text-align: right;
  }
  .person-name {
    font-weight: 700; font-size: 28px; color: var(--sky);
  }
  .person-title {
    font-weight: 500; font-size: 14px; letter-spacing: 1px;
    color: var(--ink); text-transform: uppercase; margin-top: 2px;
  }
  .address {
    position: absolute; left: 48px; top: 250px;
    font-size: 16px; font-weight: 500; color: var(--muted);
  }
  .contact-list {
    position: absolute; left: 48px; top: 284px;
    list-style: none;
  }
  .contact-list li {
    display: flex; align-items: center; gap: 12px;
    font-size: 16px; font-weight: 500; color: var(--muted);
    height: 30px;
  }
  .contact-list svg { width: 18px; height: 18px; flex: none; }
  .brand-disc {
    position: absolute; right: 40px; top: 110px;
    width: 210px; height: 210px; border-radius: 50%;
    background: var(--sky);
  }
</style>
</head>
<body>
  <section class="card card-front" aria-label="Business card front">
    <div class="front-pattern" role="img" aria-label="Repeating tonal brand pattern in light and deep blue"></div>
    <div class="front-lockup">
      <span class="lockup-dot"></span>
      <span class="wordmark">BRIM<br>Outreach Partners</span>
    </div>
  </section>

  <section class="card card-back" aria-label="Business card back">
    <span class="back-tab"></span>
    <div class="wordmark back-wordmark">BRIM<br>Outreach Partners</div>
    <div class="person">
      <p class="person-name">Marcus Dell-Hayes</p>
      <p class="person-title">Managing Partner</p>
    </div>
    <p class="address">PO Box 41270, Franklin, TN 37064</p>
    <ul class="contact-list">
      <li>
        <svg viewBox="0 0 24 24" aria-hidden="true"><path fill="#4ab3e6" d="M6.6 10.8a15.1 15.1 0 0 0 6.6 6.6l2.2-2.2a1 1 0 0 1 1-.25 11.4 11.4 0 0 0 3.6.57 1 1 0 0 1 1 1V20a1 1 0 0 1-1 1A17 17 0 0 1 3 4a1 1 0 0 1 1-1h3.5a1 1 0 0 1 1 1c0 1.25.2 2.45.57 3.57a1 1 0 0 1-.25 1z"/></svg>
        +945-555-0147
      </li>
      <li>
        <svg viewBox="0 0 24 24" aria-hidden="true"><rect x="2" y="5" width="20" height="14" rx="2" fill="#4ab3e6"/><path d="M3 6l9 7 9-7" stroke="#fff" stroke-width="1.6" fill="none"/></svg>
        marcus@brimoutreachpartners.com
      </li>
      <li>
        <svg viewBox="0 0 24 24" aria-hidden="true"><circle cx="12" cy="12" r="10" fill="#4ab3e6"/><path d="M2 12h20M12 2c3 3 3 17 0 20M12 2c-3 3-3 17 0 20" stroke="#fff" stroke-width="1.3" fill="none"/></svg>
        www.brimoutreachpartners.com
      </li>
    </ul>
    <span class="brand-disc"></span>
  </section>
</body>
</html>
```